Business Card Design Project

use presentation folder design and my logo and make 4 over 4 business cards

Industry/Entity Type

Business

Requirements
Must have
• use the design from my presentation folder and put my logo on it

Name
Title
phone
fax
email

```html
<!DOCTYPE html>
<html lang="en">
<head>
<meta charset="utf-8">
<title>Kindred Path Counseling – Business Cards</title>
<link href="https://fonts.googleapis.com/css2?family=Tinos:wght@400;700&display=swap" rel="stylesheet">
<style>
  :root {
    --stage: #ecebe8;
    --card-white: #f7f6f4;
    --card-front: #efedea;
    --panel-beige: #e6ddcf;
    --band-brown: #a0692d;
    --accent-brown: #a65a22;
    --soft-grey: #e4e3e1;
    --ink: #2a2a2a;
  }
  * { margin: 0; padding: 0; box-sizing: border-box; }
  html, body {
    width: 1200px; height: 900px; overflow: hidden;
    background: var(--stage);
    font-family: "Tinos", "Times New Roman", serif;
  }
  .canvas { position: relative; width: 1200px; height: 900px; }
  .card {
    position: absolute; width: 630px; height: 360px;
    overflow: hidden; border-radius: 2px;
    box-shadow: 0 6px 18px rgba(0,0,0,.18);
  }
  .card--front { left: 285px; top: 70px; background: var(--card-front); }
  .card--back  { left: 285px; top: 470px; background: var(--card-white); }
  .card__shapes { position: absolute; inset: 0; width: 100%; height: 100%; }

  .brand-lockup {
    position: absolute; left: 0; right: 0; top: 150px;
    display: flex; align-items: center; justify-content: center; gap: 16px;
  }
  .brand-lockup__dot {
    width: 34px; height: 34px; border-radius: 50%; background: var(--accent-brown);
  }
  .brand-lockup__name {
    font-size: 40px; font-weight: 400; color: var(--accent-brown); letter-spacing: .5px;
  }

  .brand-mini {
    position: absolute; left: 124px; top: 70px;
    display: flex; align-items: center; gap: 10px;
  }
  .brand-mini__dot { width: 20px; height: 20px; border-radius: 50%; background: var(--accent-brown); }
  .brand-mini__name { font-size: 18px; color: var(--accent-brown); line-height: 1.1; width: 110px; }

  .contact-person { position: absolute; left: 282px; top: 78px; color: var(--ink); }
  .contact-person__name { font-size: 30px; font-weight: 400; letter-spacing: 1.5px; }
  .contact-person__title { font-size: 18px; margin-top: 2px; }

  .contact-list {
    position: absolute; left: 270px; top: 168px;
    list-style: none; font-size: 18px; color: var(--ink); line-height: 24px;
  }
  .contact-list__label {
    display: inline-block; width: 24px; font-weight: 700; color: var(--accent-brown);
  }
</style>
</head>
<body>
<main class="canvas">

  <section class="card card--front" aria-label="Business card front">
    <svg class="card__shapes" viewBox="0 0 630 360" aria-hidden="true">
      <circle cx="480" cy="40" r="46" fill="#e8e1da"/>
      <circle cx="235" cy="60" r="40" fill="#e7e6e4"/>
    </svg>
    <div class="brand-lockup">
      <span class="brand-lockup__dot"></span>
      <span class="brand-lockup__name">Kindred Path Counseling</span>
    </div>
  </section>

  <section class="card card--back" aria-label="Business card back">
    <svg class="card__shapes" viewBox="0 0 630 360" aria-hidden="true">
      <path d="M0 0 H95 Q70 60 62 160 L0 180 Z" fill="var(--soft-grey)"/>
      <path d="M140 8 H590 Q630 8 630 48 V360 H350 L336 305 Q324 262 285 258 L150 246 Q108 242 108 200 V40 Q108 8 140 8 Z" fill="var(--panel-beige)"/>
      <path d="M0 262 H270 Q300 262 308 290 L326 360 H0 Z" fill="var(--band-brown)"/>
    </svg>
    <div class="brand-mini">
      <span class="brand-mini__dot"></span>
      <span class="brand-mini__name">Kindred Path</span>
    </div>
    <div class="contact-person">
      <h1 class="contact-person__name">DANIEL MARSH</h1>
      <p class="contact-person__title">Operation Manager</p>
    </div>
    <ul class="contact-list">
      <li><span class="contact-list__label">T</span>(555) 21 604 18 32</li>
      <li><span class="contact-list__label">F</span>(555) 21 604 18 47</li>
      <li><span class="contact-list__label">E</span>daniel@kindredpathcounseling.com</li>
    </ul>
  </section>

</main>
</body>
</html>
```